Super Stunning and Creative 1-page Infographic Needed

Take the attached content and covert it into a 1-page 8.5x11" stunning, and highly engaging infographic. The infographic must:

* Use Birch Supply colors
* Have icons and graphics used appropriately
* Look unique and creative, and super cool
* Be very eye catching

See attachment for content.

The topic is about retail inventory management. Retail = Store. Not warehouse looking. If you can add Birch Supply photos, this may enhance it. Just a consideration, but not necessary.

Target Market(s)

Birch Supply Store Owners

Industry/Entity Type

Retail Industry - Home Improvement

Font styles to use
Sans Serif

Requirements
Must have
• Birch Supply Colors, Super Creative, Stunning and Eye Capturing. Graphics and icons where they make sense.
Should not have
• Common infographic look. It must look different.

```html
<!DOCTYPE html>
<html lang="en">
<head>
<meta charset="utf-8">
<title>Eight Misconceptions about Managing Your Inventory Debunked</title>
<link href="https://fonts.googleapis.com/css2?family=Barlow:wght@400;600;700;800&family=Barlow+Condensed:wght@600;700&family=Montserrat:wght@800&display=swap" rel="stylesheet">
<style>
  :root {
    --brand-red: #d9163f;
    --title-gray: #6d6e71;
    --band-gray: #dcdcde;
    --band-edge: #c6c7c9;
    --ink: #3a3a3c;
    --paper: #ffffff;
    --backdrop: #e9e9ec;
  }
  * { box-sizing: border-box; margin: 0; padding: 0; }
  html, body { width: 1200px; height: 800px; overflow: hidden; }
  body {
    background: var(--backdrop);
    font-family: "Barlow", Arial, sans-serif;
    color: var(--ink);
    display: flex; align-items: center; justify-content: center;
  }
  .sheet {
    width: 600px; height: 776px;
    background: var(--paper);
    padding: 22px 22px 16px;
    box-shadow: 0 2px 10px rgba(0,0,0,.12);
    display: flex; flex-direction: column;
  }
  .title-bar {
    background: var(--title-gray);
    color: #fff;
    font-family: "Barlow Condensed", Arial, sans-serif;
    font-weight: 700;
    font-size: 19px;
    white-space: nowrap;
    padding: 6px 14px;
    margin-right: 30px;
    clip-path: polygon(0 0, 100% 0, 97% 100%, 0 100%);
  }
  .myths { list-style: none; margin-top: 6px; }
  .myth {
    display: grid;
    grid-template-columns: 88px 1fr 80px;
    height: 70px;
    margin-bottom: 2px;
  }
  .myth-number {
    background: var(--brand-red);
    color: #fff;
    font-family: "Montserrat", Arial, sans-serif;
    font-weight: 800;
    font-size: 30px;
    display: flex; align-items: flex-end; justify-content: flex-start;
    padding: 0 0 8px 18px;
    margin-top: 14px;
    clip-path: polygon(0 22%, 62% 0, 100% 100%, 0 100%);
  }
  .myth-band {
    background: var(--band-gray);
    border-top: 6px solid var(--band-edge);
    padding: 5px 10px 4px 8px;
    font-size: 7.7px;
    line-height: 1.28;
    display: flex; flex-direction: column; justify-content: center;
  }
  .myth-claim { font-weight: 700; font-size: 8.6px; color: #2b2b2d; margin-bottom: 2px; }
  .myth-icon {
    background: var(--brand-red);
    display: flex; align-items: center; justify-content: center;
    clip-path: polygon(10% 0, 100% 0, 100% 100%, 0 100%, 6% 70%, 0 45%, 8% 20%);
  }
  .myth-icon svg { width: 42px; height: 42px; fill: none; stroke: #fff; stroke-width: 1.6; stroke-linecap: round; stroke-linejoin: round; }

  .sheet-footer {
    margin-top: auto;
    display: grid;
    grid-template-columns: 130px 1fr;
    gap: 12px;
    align-items: end;
  }
  .program-name {
    font-weight: 700;
    font-size: 15px;
    line-height: 1.15;
    color: var(--brand-red);
  }
  .footer-copy { font-size: 8.4px; line-height: 1.35; margin-bottom: 10px; }
  .footer-row { display: flex; align-items: flex-end; gap: 16px; white-space: nowrap; }
  .brand-name { display: flex; align-items: center; gap: 5px; font-weight: 700; font-size: 13px; color: var(--brand-red); }
  .brand-name i { width: 9px; height: 9px; background: var(--brand-red); display: inline-block; }
  .dept { font-weight: 700; font-size: 10px; color: var(--title-gray); border-left: 1px solid var(--band-edge); padding-left: 8px; }
  .contact h3 { color: var(--brand-red); font-size: 10px; font-weight: 700; margin-bottom: 2px; }
  .contact p { font-size: 9px; font-weight: 600; display: flex; gap: 12px; }
  .contact span { display: inline-flex; align-items: center; }
  .contact b { display: inline-block; width: 7px; height: 7px; border-radius: 50%; background: var(--brand-red); margin-right: 4px; }
</style>
</head>
<body>
<main class="sheet">
  <h1 class="title-bar">Eight Misconceptions about Managing Your Inventory Debunked</h1>

  <ol class="myths">
    <li class="myth">
      <div class="myth-number">1</div>
      <div class="myth-band">
        <p class="myth-claim">Getting my replenishment settings right is the most important way to manage inventory</p>
        <p>Maintaining strong inventory record accuracy (IRA) is the most critical factor toward staying in stock, addressing dead inventory and driving incremental profitability.</p>
      </div>
      <div class="myth-icon"><svg viewBox="0 0 40 40"><rect x="9" y="7" width="20" height="27" rx="1"/><rect x="15" y="4" width="8" height="5"/><path d="M13 15h12M13 20h12M13 25h8M31 14l-7 12"/></svg></div>
    </li>
    <li class="myth">
      <div class="myth-number">2</div>
      <div class="myth-band">
        <p class="myth-claim">When sales have slowed, inventory needs cutting</p>
        <p>Efforts to reduce inventory can be lethal, creating out of stocks, empty shelves, poor store image perception &amp; frustrated customers who will ultimately shop the competition. Instead, if inventories need to be reduced, prioritize by looking at unproductive products taking a more strategic approach to healthier inventory levels.</p>
      </div>
      <div class="myth-icon"><svg viewBox="0 0 40 40"><path d="M6 16l14-9 14 9v18H6z"/><rect x="11" y="20" width="8" height="7"/><rect x="21" y="20" width="8" height="7"/><rect x="16" y="27" width="8" height="7"/><path d="M8 6l6 6M14 7v5H9"/></svg></div>
    </li>
    <li class="myth">
      <div class="myth-number">3</div>
      <div class="myth-band">
        <p class="myth-claim">Dead stock (stuff that hasn't sold in years) needs to be marked down &amp; moved out</p>
        <p>Leverage markdowns as a last resort. Instead, first check to see if the product is even physically in the store, priced competitively, redundant product in the set, or merchandised effectively. More times than not you can move product without having to sell it at a discount.</p>
      </div>
      <div class="myth-icon"><svg viewBox="0 0 40 40"><path d="M5 17l15-10 15 10M8 15v19h24V15"/><rect x="14" y="22" width="12" height="12"/><path d="M14 28h12M20 22v12"/><circle cx="20" cy="15" r="3"/></svg></div>
    </li>
    <li class="myth">
      <div class="myth-number">4</div>
      <div class="myth-band">
        <p class="myth-claim">Working my Maple count sheets will drive sustainable improvements to IRA</p>
        <p>If used to update and correct counts with no regard toward understanding what caused the issues, then this is a band-aid approach and typically won't provide much long-term IRA gain. Instead, work count sheets to understand the root of operational gaps and retrain staff as necessary for sustainable improvements.</p>
      </div>
      <div class="myth-icon"><svg viewBox="0 0 40 40"><path d="M10 22V8M6 12l4-4 4 4M20 18V5M16 9l4-4 4 4M30 22V8M26 12l4-4 4 4"/><circle cx="13" cy="30" r="4"/><circle cx="27" cy="30" r="4"/><circle cx="13" cy="30" r="1.2"/><circle cx="27" cy="30" r="1.2"/></svg></div>
    </li>
    <li class="myth">
      <div class="myth-number">5</div>
      <div class="myth-band">
        <p class="myth-claim">Increasing my inventory depth will hurt profits and drive down my inventory turns</p>
        <p>Stores who have deeper levels of inventory outperform stores that don't. When focused on raising inventory strategically through programs like economic order quantities, minimum order points, and preseason planner, inventory turns typically remain the same as inventory increases.</p>
      </div>
      <div class="myth-icon"><svg viewBox="0 0 40 40"><circle cx="25" cy="23" r="9"/><path d="M25 18v10M27.5 20h-3.5a1.8 1.8 0 000 3.6h2a1.8 1.8 0 010 3.6h-3.5"/><path d="M7 34V20M4 23l3-4 3 4M6 34h10v-5H6"/></svg></div>
    </li>
    <li class="myth">
      <div class="myth-number">6</div>
      <div class="myth-band">
        <p class="myth-claim">Spending more than an hour (or more) working the 'RSO' will result in better quality suggested orders</p>
        <p>Typically, if it takes greater than 60 minutes to work your RSO each week per store, there are larger issues at play. The goal is to be able to review the RSO on an exception basis for outliers and transmit it through to then shift focus on other important store activities.</p>
      </div>
      <div class="myth-icon"><svg viewBox="0 0 40 40"><rect x="6" y="8" width="18" height="26" rx="1"/><rect x="11" y="5" width="8" height="5"/><path d="M10 17l2 2 3-3M10 25l2 2 3-3M18 18h3M18 26h3"/><path d="M24 22l6-3 6 3v7l-6 3-6-3z"/></svg></div>
    </li>
    <li class="myth">
      <div class="myth-number">7</div>
      <div class="myth-band">
        <p class="myth-claim">Carry more weeks of supply on fast moving products and less on slower velocity SKUs</p>
        <p>Based on how Kestrel Retail calculates order points, this can result in overstocking on faster goods and insufficient amounts of slower ones. Revisit your weeks of supply settings to ensure they are maintained at or near Birch best practice levels.</p>
      </div>
      <div class="myth-icon"><svg viewBox="0 0 40 40"><path d="M16 12l10-5 10 5v12l-10 5-10-5z"/><path d="M16 12l10 5 10-5M26 17v12"/><path d="M4 18h8M6 23h8M3 28h9"/></svg></div>
    </li>
    <li class="myth">
      <div class="myth-number">8</div>
      <div class="myth-band">
        <p class="myth-claim">With the onset of global supply chain issues, reaching a 95% in-stock position is next to impossible</p>
        <p>Undoubtedly, the industry supply problems make obtaining a higher in-stock position more challenging, but still quite probable. The key is to focus on what you are able to control within the four walls of your operations &amp; consistently execute the basics (i.e. count sheets, shooting the outs, item change management).</p>
      </div>
      <div class="myth-icon"><svg viewBox="0 0 40 40"><rect x="5" y="7" width="30" height="21" rx="1"/><path d="M16 34h8M20 28v6M22 11l-5 8h6l-4 7"/></svg></div>
    </li>
  </ol>

  <footer class="sheet-footer">
    <p class="program-name">Inventory Management</p>
    <div>
      <p class="footer-copy">See the Birch Way of Retailing Inventory Management section for further insights and practices to optimize inventory health.<br>Pathway: BIRCHNET &gt;&gt; About Birch &gt;&gt; Birch Way of Retailing &gt;&gt; Inventory Management</p>
      <div class="footer-row">
        <span class="brand-name"><i></i>Birch Supply</span>
        <span class="dept">Store Systems &amp; Operations</span>
        <div class="contact">
          <h3>CONTACT INFORMATION:</h3>
          <p><span><b></b>555.014.2290</span><span><b></b>storeops@birchsupply.example</span></p>
        </div>
      </div>
    </div>
  </footer>
</main>
</body>
</html>
```